Full redesign of dairy products including Yogurts and milk products

We have been selling milk and yogurts over the past 15 years, we are now expanding into a wider range of dairy products to include flavoured milk and a variety of soft cheeses such as cottage cheese etc. It is now the perfect time to redesign our existing product range to give a fresh and new look to our products. Have a look at our website https://rtvale.co.uk/ for further details. We are rebranding as NUVELKA, I have attached a identify pack to give you a feel of the the design, this is a fresh and bright design that will reflect the fresh and tasteful products we produce. The current milk label cut out is unique to us and I would like to continue using this shape which I have attached, the other labels should be done using regular rectangular rounded edge labels. The following designs are required;
1 x Universal lid (71.5mm) design for all below 120ml Yogurts
-11 x 120 ml Yogurt pot designs
Strawberry
Strawberry Banana
Peach & Apricot
Cherry
Toffee
Vanilla
Natural
Orange
Forest Fruits
Pineapple
Mango
1 x Universal lid (95.5mm)for below yogurts (can be identical to the 120ml Lid)
-4 x 450ml Yogurt Pots
Strawberry
Natural
Toffee
Mango
-1 x Universal (95.5mm) LID for 150ml Greek Yogurt
-4 x Designs for 150ml Greek yogurt POT
Strawberry
Natural
Vanilla
Mango

3 x Flavoured milk labels 2 sizes 250ml & 1lt
Biscotti
Chocolate
Strawberry

Cottage Cheese Lid & Pot 250g

1 x Quark universal Lid (95.5mm)
4 x Quark 250g pots
Natural
Strawberry
Peach & Apricot
Mango

```html
<!DOCTYPE html>
<html lang="en">
<head>
<meta charset="utf-8">
<title>NUVELKA Strawberry Yogurt – Lid and Pot Labels</title>
<link rel="stylesheet" href="https://fonts.googleapis.com/css2?family=Grandstander:wght@600;700;800;900&family=Rubik:wght@500;700&display=swap">
<style>
  :root {
    --berry-red: #e3262f;
    --deep-red: #c81d27;
    --cream: #ffffff;
    --milk: #f4f2f0;
    --canvas: #f3f3f3;
  }
  html, body {
    margin: 0;
    padding: 0;
    width: 1200px;
    height: 819px;
    overflow: hidden;
    background: var(--canvas);
  }
  .artboard { display: block; width: 1200px; height: 819px; }
  .brand-name { font-family: "Grandstander", sans-serif; font-weight: 800; fill: var(--cream); letter-spacing: 1px; }
  .tagline { font-family: "Grandstander", sans-serif; font-weight: 600; fill: var(--cream); }
  .product-type { font-family: "Grandstander", sans-serif; font-weight: 900; fill: var(--cream); }
  .flavour { font-family: "Grandstander", sans-serif; font-weight: 700; fill: var(--cream); }
  .weight { font-family: "Rubik", sans-serif; font-weight: 500; fill: var(--cream); }
  .natural-badge { fill: var(--cream); }
  .natural-text { font-family: "Rubik", sans-serif; font-weight: 700; fill: var(--berry-red); }
  .blurb { font-family: "Rubik", sans-serif; font-weight: 700; fill: var(--cream); }
  .lid-base, .label-base { fill: var(--berry-red); }
  .lid-rim { fill: none; stroke: var(--deep-red); stroke-width: 3; }
  .milk-band { fill: var(--milk); }
</style>
</head>
<body>
<svg class="artboard" viewBox="0 0 1200 819" xmlns="http://www.w3.org/2000/svg">
  <defs>
    <clipPath id="lid-shape"><circle cx="0" cy="0" r="200"/></clipPath>
    <clipPath id="label-shape"><rect x="0" y="0" width="440" height="210" rx="14"/></clipPath>
    <radialGradient id="splash-tone" cx="0.5" cy="0.5" r="0.6">
      <stop offset="0" stop-color="#ffffff"/>
      <stop offset="1" stop-color="#e9e6e4"/>
    </radialGradient>
    <linearGradient id="berry-tone" x1="0" y1="0" x2="0" y2="1">
      <stop offset="0" stop-color="#d93a3a"/>
      <stop offset="1" stop-color="#b01b22"/>
    </linearGradient>
  </defs>

  <!-- 120g lid -->
  <g class="lid lid-small" transform="translate(300 290) scale(0.95)">
    <circle class="lid-base" r="200"/>
    <g clip-path="url(#lid-shape)">
      <path role="img" aria-label="Milk splash illustration" fill="url(#splash-tone)"
            d="M120 20 C160 0 190 -10 210 -20 L210 210 L-160 210 C-120 160 -40 150 20 150 C90 140 110 80 120 20 Z"/>
    </g>
    <circle class="lid-rim" r="198"/>
    <text class="brand-name" x="0" y="-118" text-anchor="middle" font-size="40">NUVELKA</text>
    <text class="tagline" x="0" y="-98" text-anchor="middle" font-size="13">Dairy Goodness</text>
    <text class="product-type" x="0" y="-30" text-anchor="middle" font-size="64">yogurt</text>
    <text class="weight" x="-168" y="12" font-size="20">120g</text>
    <text class="flavour" x="20" y="14" text-anchor="middle" font-size="30">Strawberry</text>
    <rect class="natural-badge" x="-180" y="28" width="82" height="20" rx="6"/>
    <text class="natural-text" x="-139" y="42" text-anchor="middle" font-size="10">100% natural</text>
    <text class="blurb" x="20" y="60" text-anchor="middle" font-size="13">Lorem ipsum Lorem ipsum</text>
    <text class="blurb" x="20" y="77" text-anchor="middle" font-size="13">dolor sit amet, consecte</text>
    <rect role="img" aria-label="Fresh strawberries illustration" fill="url(#berry-tone)" x="-80" y="100" width="160" height="64" rx="32"/>
  </g>

  <!-- 250g lid -->
  <g class="lid lid-large" transform="translate(830 290) scale(1.2)">
    <circle class="lid-base" r="200"/>
    <g clip-path="url(#lid-shape)">
      <path role="img" aria-label="Milk splash illustration" fill="url(#splash-tone)"
            d="M120 20 C160 0 190 -10 210 -20 L210 210 L-160 210 C-120 160 -40 150 20 150 C90 140 110 80 120 20 Z"/>
    </g>
    <circle class="lid-rim" r="198"/>
    <text class="brand-name" x="0" y="-118" text-anchor="middle" font-size="40">NUVELKA</text>
    <text class="tagline" x="0" y="-98" text-anchor="middle" font-size="13">Dairy Goodness</text>
    <text class="product-type" x="10" y="-30" text-anchor="middle" font-size="64">yogurt</text>
    <text class="weight" x="-182" y="-36" font-size="20">250g</text>
    <text class="flavour" x="20" y="14" text-anchor="middle" font-size="30">Strawberry</text>
    <rect class="natural-badge" x="-182" y="-12" width="82" height="20" rx="6"/>
    <text class="natural-text" x="-141" y="2" text-anchor="middle" font-size="10">100% natural</text>
    <text class="blurb" x="20" y="60" text-anchor="middle" font-size="13">Lorem ipsum Lorem ipsum</text>
    <text class="blurb" x="20" y="77" text-anchor="middle" font-size="13">dolor sit amet, consecte</text>
    <rect role="img" aria-label="Fresh strawberries illustration" fill="url(#berry-tone)" x="-80" y="100" width="160" height="64" rx="32"/>
  </g>

  <!-- 120g pot wrap label -->
  <g class="pot-label label-small" transform="translate(80 580)">
    <g clip-path="url(#label-shape)">
      <rect class="label-base" width="440" height="210"/>
      <path class="milk-band" d="M0 182 C120 160 300 205 440 175 L440 210 L0 210 Z"/>
      <rect role="img" aria-label="Milk splash illustration" fill="url(#splash-tone)" x="340" y="18" width="84" height="36" rx="18"/>
      <rect role="img" aria-label="Strawberries illustration" fill="url(#berry-tone)" x="14" y="70" width="58" height="70" rx="22"/>
      <rect role="img" aria-label="Strawberries illustration" fill="url(#berry-tone)" x="362" y="78" width="58" height="70" rx="22"/>
    </g>
    <text class="brand-name" x="220" y="40" text-anchor="middle" font-size="28">NUVELKA</text>
    <text class="tagline" x="220" y="56" text-anchor="middle" font-size="10">Dairy Goodness</text>
    <text class="product-type" x="220" y="96" text-anchor="middle" font-size="32">milk</text>
    <text class="product-type" x="225" y="128" text-anchor="middle" font-size="32">&amp; yogurt</text>
    <text class="flavour" x="235" y="154" text-anchor="middle" font-size="16">Strawberry</text>
    <rect class="natural-badge" x="86" y="144" width="64" height="16" rx="5"/>
    <text class="natural-text" x="118" y="155" text-anchor="middle" font-size="8">100% natural</text>
  </g>

  <!-- 250g pot wrap label -->
  <g class="pot-label label-large" transform="translate(600 580)">
    <g clip-path="url(#label-shape)">
      <rect class="label-base" width="440" height="210"/>
      <path class="milk-band" d="M0 182 C120 160 300 205 440 175 L440 210 L0 210 Z"/>
      <rect role="img" aria-label="Milk splash illustration" fill="url(#splash-tone)" x="340" y="18" width="84" height="36" rx="18"/>
      <rect role="img" aria-label="Strawberries illustration" fill="url(#berry-tone)" x="14" y="70" width="58" height="70" rx="22"/>
      <rect role="img" aria-label="Strawberries illustration" fill="url(#berry-tone)" x="362" y="78" width="58" height="70" rx="22"/>
    </g>
    <text class="brand-name" x="220" y="40" text-anchor="middle" font-size="28">NUVELKA</text>
    <text class="tagline" x="220" y="56" text-anchor="middle" font-size="10">Dairy Goodness</text>
    <text class="product-type" x="220" y="96" text-anchor="middle" font-size="32">milk</text>
    <text class="product-type" x="225" y="128" text-anchor="middle" font-size="32">&amp; yogurt</text>
    <text class="flavour" x="235" y="154" text-anchor="middle" font-size="16">Strawberry</text>
    <rect class="natural-badge" x="86" y="144" width="64" height="16" rx="5"/>
    <text class="natural-text" x="118" y="155" text-anchor="middle" font-size="8">100% natural</text>
  </g>
</svg>
</body>
</html>
```